Dietitian clinic needs a business card design

We need a business card design for a new dietitian group based in Singapore called "Brightpath and Bloom". We provide expert, personalised nutrition care to support a wide range of health needs, from chronic conditions to mindful eating. Our team also offers consulting, speaking, and tailored solutions for healthcare providers, organisations, and food services.

Target Market(s)

Adults

Industry/Entity Type

Healthcare

Contact Information for Business Card

Name, position, contact number, email, website address, our logo

Requirements
Nice to have
• Clean, professional but welcoming look

```html
<!DOCTYPE html>
<html lang="en">
<head>
<meta charset="utf-8">
<title>Brightpath and Bloom — Business Card</title>
<link rel="stylesheet" href="https://fonts.googleapis.com/css2?family=Playfair+Display:wght@800&family=Open+Sans:wght@400;600&display=swap">
<style>
  :root {
    --stage: #26272a;
    --teal-deep: #1d4f63;
    --teal: #225e6d;
    --teal-light: #2a6975;
    --blush: #e3a4a4;
    --ink-light: #ffffff;
    --line: rgba(255,255,255,0.75);
  }
  * { box-sizing: border-box; margin: 0; padding: 0; }
  html, body { width: 1200px; height: 840px; overflow: hidden; background: var(--stage); }
  .canvas {
    width: 1200px; height: 840px;
    display: flex; flex-direction: column; align-items: center; justify-content: center; gap: 40px;
  }
  .card {
    position: relative;
    width: 620px; height: 354px;
    border-radius: 24px;
    background: radial-gradient(circle at 45% 60%, var(--teal-deep), var(--teal) 55%, var(--teal-light));
    box-shadow: 0 5px 0 var(--blush);
    overflow: hidden;
  }
  .wordmark {
    font-family: "Playfair Display", Georgia, serif;
    font-weight: 800;
    color: var(--blush);
    line-height: 0.9;
    letter-spacing: -0.5px;
  }
  /* Front */
  .front-pattern {
    position: absolute; inset: 0;
    background: radial-gradient(ellipse at 40% 85%, #1f5670 0%, #1e5564 45%, #235f6c 100%);
  }
  .front .brand {
    position: absolute; top: 60px; right: 56px;
    display: flex; align-items: center; gap: 18px;
  }
  .front .brand-dot { width: 34px; height: 34px; border-radius: 50%; background: var(--blush); }
  .front .wordmark { font-size: 54px; text-align: right; }
  /* Back */
  .back .brand {
    position: absolute; top: 58px; left: 0; right: 0;
    display: flex; justify-content: center; align-items: center; gap: 16px;
  }
  .back .brand-dot { width: 22px; height: 22px; border-radius: 50%; background: var(--blush); }
  .back .wordmark { font-size: 38px; }
  .details {
    position: absolute; top: 168px; left: 0; right: 0;
    display: flex; justify-content: center; align-items: center; gap: 24px;
  }
  .person { text-align: right; }
  .person-name {
    font-family: "Playfair Display", Georgia, serif; font-weight: 800;
    color: var(--blush); font-size: 24px; letter-spacing: 0.5px;
  }
  .person-role {
    font-family: "Open Sans", Arial, sans-serif; color: var(--ink-light);
    font-size: 17px; margin-top: 2px;
  }
  .divider { width: 1px; height: 82px; background: var(--line); }
  .contacts { list-style: none; font-family: "Open Sans", Arial, sans-serif; color: var(--ink-light); font-size: 16px; }
  .contacts li { display: flex; align-items: center; gap: 8px; line-height: 1.6; }
  .contacts svg { width: 14px; height: 14px; flex: none; }
  .address {
    position: absolute; bottom: 42px; left: 0; right: 0; text-align: center;
    font-family: "Open Sans", Arial, sans-serif; color: var(--ink-light); font-size: 17px;
  }
</style>
</head>
<body>
<main class="canvas">
  <section class="card front">
    <div class="front-pattern" role="img" aria-label="Flowing contour line pattern in deep teal"></div>
    <div class="brand">
      <span class="brand-dot"></span>
      <p class="wordmark">Brightpath<br>and Bloom</p>
    </div>
  </section>

  <section class="card back">
    <div class="brand">
      <span class="brand-dot"></span>
      <p class="wordmark">Brightpath and Bloom</p>
    </div>
    <div class="details">
      <div class="person">
        <p class="person-name">DANIEL REYES</p>
        <p class="person-role">Managing Director</p>
      </div>
      <span class="divider"></span>
      <ul class="contacts">
        <li>
          <svg viewBox="0 0 16 16" aria-hidden="true"><path fill="#e3a4a4" d="M4 1l2.5 3-1.5 2c1 2 3 4 5 5l2-1.5 3 2.5-2 2C7 14 2 9 2 3z"/></svg>
          065-812 340 771
        </li>
        <li>
          <svg viewBox="0 0 16 16" aria-hidden="true"><rect x="1" y="3" width="14" height="10" rx="1.5" fill="#e3a4a4"/><path d="M1.5 4l6.5 5 6.5-5" fill="none" stroke="#225e6d" stroke-width="1.4"/></svg>
          hello@brightpathbloom.sg
        </li>
        <li>
          <svg viewBox="0 0 16 16" aria-hidden="true"><circle cx="8" cy="8" r="7" fill="#e3a4a4"/><path d="M1 8h14M8 1c-3 3-3 11 0 14M8 1c3 3 3 11 0 14" fill="none" stroke="#225e6d" stroke-width="1.1"/></svg>
          www.brightpathbloom.sg
        </li>
      </ul>
    </div>
    <p class="address">Your Address, City, State, Zip 0000</p>
  </section>
</main>
</body>
</html>
```